Stationery Design Project

Brivan-Holt Consultants is interim management company. We are specialized in finding the best Finance and IT consultants for our clients when they require additional resources on an interim basis for projects or special situations. We are flexible in our approach and we always seek to maximize the benefits for our clients as well as our consultants.

We are looking for a design of our letterhead, general stationery and business cards using the company name. The design will also be found on our coming web pages.
Updates

Please also create a logo for Brivan-Holt Consultants which expresses that we want to match the best finance and IT people to our customers projects

Target Market(s)

Larger and mid sized companies (all sectors), as well as highly skilled Finance & IT professionals/consultants

Industry/Entity Type

Business

Requirements
Must have
• Brivan-Holt Consultants
We are expecting that 'Brivan-Holt' will be on the first line and 'Consultants' on a second line.
Please also indicate style of the letters for our address/phone and mail details. Our current address is:
Tarnvoldgade 9,
2870 Kalsbro
Danmark
Mobile: +45 XX XX XX XX Mail: xx@brivan-holt.dk

```html
<!DOCTYPE html>
<html lang="da">
<head>
<meta charset="utf-8">
<title>Brivan-Holt Consultants – Stationery</title>
<link rel="stylesheet" href="https://fonts.googleapis.com/css2?family=Open+Sans:wght@300;400;600&display=swap">
<style>
  :root {
    --ink: #141414;
    --text-grey: #6d6d6d;
    --brand-red: #d4110f;
    --red-deep: #a50d0c;
    --red-light: #e2352a;
    --slate: #4a4a4a;
    --card-white: #fcfcfc;
    --stage-light: #f7f7f7;
    --stage-dark: #d9d9d9;
  }
  * { box-sizing: border-box; margin: 0; padding: 0; }
  html, body { width: 1200px; height: 839px; overflow: hidden; }
  body {
    position: relative;
    font-family: "Open Sans", Arial, sans-serif;
    background: radial-gradient(ellipse 620px 460px at 260px 160px, var(--stage-light), var(--stage-dark));
  }

  .wordmark { position: absolute; color: var(--ink); font-weight: 600; line-height: 1; white-space: nowrap; }
  .wordmark .name { display: block; text-transform: uppercase; }
  .wordmark .sub { display: block; text-transform: lowercase; }

  .hero-mark { left: 49px; top: 77px; }
  .hero-mark .name { font-size: 84px; letter-spacing: 1px; }
  .hero-mark .sub { font-size: 44px; letter-spacing: 31px; margin-top: 33px; margin-left: 2px; }

  .card {
    position: absolute;
    border-radius: 18px;
    box-shadow: 0 3px 8px rgba(0,0,0,.35);
    overflow: hidden;
  }
  .card-back {
    left: 116px; top: 338px; width: 466px; height: 268px;
    background: linear-gradient(120deg, var(--red-light) 0%, var(--brand-red) 45%, var(--red-deep) 100%);
  }
  .card-back .wordmark { color: #fff; right: 28px; top: 190px; }
  .card-back .name { font-size: 32px; letter-spacing: .3px; }
  .card-back .sub { font-size: 18px; letter-spacing: 10.4px; margin-top: 8px; }

  .card-front { background: var(--card-white); width: 466px; height: 268px; }
  .card-a { left: 667px; top: 216px; }
  .card-b { left: 642px; top: 507px; }

  .person { position: absolute; font-size: 17px; font-weight: 600; color: var(--ink); line-height: 1.1; }
  .person .surname { color: var(--brand-red); }
  .role { display: block; font-size: 14px; font-weight: 400; color: var(--text-grey); letter-spacing: .4px; margin-top: 3px; }

  .address, .contacts { position: absolute; list-style: none; font-size: 12.5px; font-weight: 300; color: var(--text-grey); line-height: 17px; }
  .contacts li { display: flex; align-items: center; gap: 6px; }
  .contacts svg { width: 9px; height: 9px; flex: none; }

  .card-a .person { left: 23px; top: 28px; }
  .card-a .address { left: 23px; top: 84px; }
  .card-a .contacts { left: 27px; top: 137px; }
  .card-a .wordmark { right: 20px; top: 198px; text-align: left; }

  .card-b .wordmark { left: 29px; top: 40px; }
  .card-b .address { left: 27px; top: 128px; }
  .card-b .contacts { left: 31px; top: 191px; }
  .card-b .person { right: 26px; top: 169px; text-align: right; }

  .card-front .wordmark .name { font-size: 30px; letter-spacing: .3px; }
  .card-front .wordmark .sub { font-size: 16px; letter-spacing: 9.6px; margin-top: 8px; color: var(--ink); }

  .card-band { position: absolute; left: 0; bottom: 0; width: 100%; height: 20px; }
</style>
</head>
<body>

  <div class="wordmark hero-mark">
    <span class="name">Brivan-Holt</span>
    <span class="sub">consultants</span>
  </div>

  <div class="card card-back">
    <div class="wordmark">
      <span class="name">Brivan-Holt</span>
      <span class="sub">consultants</span>
    </div>
  </div>

  <div class="card card-front card-a">
    <p class="person">Mikkel <span class="surname">Aronsen</span><span class="role">Marketing Manager</span></p>
    <ul class="address">
      <li>Tarnvoldgade 9,</li>
      <li>2870 Kalsbro</li>
      <li>Danmark</li>
    </ul>
    <ul class="contacts">
      <li><svg viewBox="0 0 10 10" aria-hidden="true"><rect x="0" y="7" width="2" height="3" fill="#d4110f"/><rect x="2.7" y="5" width="2" height="5" fill="#d4110f"/><rect x="5.4" y="2.5" width="2" height="7.5" fill="#d4110f"/><rect x="8" y="0" width="2" height="10" fill="#d4110f"/></svg>+45 31 62 08 47</li>
      <li><svg viewBox="0 0 10 10" aria-hidden="true"><rect x=".6" y="2" width="8.8" height="6" fill="none" stroke="#d4110f" stroke-width="1"/><path d="M.6 2 5 5.6 9.4 2" fill="none" stroke="#d4110f" stroke-width="1"/></svg>mikkel@brivan-holt.dk</li>
      <li><svg viewBox="0 0 10 10" aria-hidden="true"><circle cx="5" cy="5" r="4.6" fill="#d4110f"/><path d="M.5 5h9M5 .5v9M2 2.5c2 1 4 1 6 0M2 7.5c2-1 4-1 6 0" stroke="#fff" stroke-width=".7" fill="none"/></svg>www.brivan-holt.dk</li>
    </ul>
    <div class="wordmark">
      <span class="name">Brivan-Holt</span>
      <span class="sub">consultants</span>
    </div>
  </div>

  <div class="card card-front card-b">
    <div class="wordmark">
      <span class="name">Brivan-Holt</span>
      <span class="sub">consultants</span>
    </div>
    <ul class="address">
      <li>Tarnvoldgade 9,</li>
      <li>2870 Kalsbro</li>
      <li>Danmark</li>
    </ul>
    <ul class="contacts">
      <li><svg viewBox="0 0 10 10" aria-hidden="true"><rect x="0" y="7" width="2" height="3" fill="#d4110f"/><rect x="2.7" y="5" width="2" height="5" fill="#d4110f"/><rect x="5.4" y="2.5" width="2" height="7.5" fill="#d4110f"/><rect x="8" y="0" width="2" height="10" fill="#d4110f"/></svg>+45 31 62 08 47</li>
      <li><svg viewBox="0 0 10 10" aria-hidden="true"><rect x=".6" y="2" width="8.8" height="6" fill="none" stroke="#d4110f" stroke-width="1"/><path d="M.6 2 5 5.6 9.4 2" fill="none" stroke="#d4110f" stroke-width="1"/></svg>mikkel@brivan-holt.dk</li>
      <li><svg viewBox="0 0 10 10" aria-hidden="true"><circle cx="5" cy="5" r="4.6" fill="#d4110f"/><path d="M.5 5h9M5 .5v9M2 2.5c2 1 4 1 6 0M2 7.5c2-1 4-1 6 0" stroke="#fff" stroke-width=".7" fill="none"/></svg>www.brivan-holt.dk</li>
    </ul>
    <p class="person">Mikkel <span class="surname">Aronsen</span><span class="role">Marketing Manager</span></p>
    <svg class="card-band" viewBox="0 0 466 20" preserveAspectRatio="none" aria-hidden="true">
      <defs>
        <linearGradient id="band-red" x1="0" x2="1">
          <stop offset="0" stop-color="#c20f0d"/>
          <stop offset=".45" stop-color="#e3140f"/>
          <stop offset="1" stop-color="#a50d0c"/>
        </linearGradient>
      </defs>
      <polygon points="0,0 282,0 274,20 0,20" fill="url(#band-red)"/>
      <polygon points="287,0 466,0 466,20 279,20" fill="#4a4a4a"/>
    </svg>
  </div>

</body>
</html>
```